Pawsome Keepers DOUBLE SIDED Flyer

I need a DOUBLE SIDED flyer design for my company "Pawsome Keepers". We offer Dog Walking, Training, and Pet Sitting (cats too!). The design should communicate reliability, caring, and honesty. Not all these photos need to be used but these are all photos of my clients. Copy can be pulled from my website www.pawsomekeepers-example.com, and you can also feel free to email me directly pawsomekeepers@mailbox-example.com with any questions.

Target Market(s)

I want to reach high end clients with pampered pets, and these flyers will be displayed in high end vet businesses. Typical clients are traveling business professionals.

Industry/Entity Type

Font styles to use
Serif
Sans Serif
Decorative

Colors
33a6d7
0592cd
33b7a4
9bcb3c

Requirements
Must have
• Mentions of:
• -green business (client files are managed online and you have access to your file that contains all vet info and house notes)
• -Picture updates daily to text or email
• -Blue Lantern and Critter Rescue AID and CPR certified
• - I am insured through Furbrook Guardians
Nice to have
• My logo is currently under revision so if the font is changed of isn't on there I wouldn't mind, I have included several options.

```html
<!DOCTYPE html>
<html lang="en">
<head>
<meta charset="utf-8">
<title>Pawsome Keepers Flyer</title>
<link rel="stylesheet" href="https://fonts.googleapis.com/css2?family=Cormorant+SC:wght@500;700&family=Shadows+Into+Light&display=swap">
<style>
  :root {
    --stage: #000000;
    --ink: #3a3b3d;
    --ink-soft: #4a4c50;
    --sky-top: #c9dcf3;
    --sky-mid: #d9e6f4;
    --sea: #8ea9c0;
    --rock: #8a7358;
    --rock-dark: #5e4d3c;
    --paper-a: #dfe6f0;
    --paper-b: #cdd8e6;
    --paper-c: #e6ecf4;
  }
  * { margin: 0; padding: 0; box-sizing: border-box; }
  html, body { width: 1200px; height: 1000px; overflow: hidden; background: var(--stage); }
  .canvas { position: relative; width: 1200px; height: 1000px; background: var(--stage); }

  .side { position: absolute; top: 111px; height: 774px; overflow: hidden; }
  .side--front { left: 0; width: 598px; }
  .side--back { left: 602px; width: 598px;
    background:
      radial-gradient(ellipse at 20% 30%, rgba(255,255,255,.45), transparent 55%),
      radial-gradient(ellipse at 80% 80%, rgba(180,195,215,.5), transparent 60%),
      linear-gradient(180deg, var(--paper-c), var(--paper-a) 50%, var(--paper-b)); }

  .front-photo { position: absolute; inset: 0;
    background: linear-gradient(180deg, var(--sky-top) 0%, var(--sky-mid) 58%, var(--sea) 63%, var(--rock) 72%, var(--rock-dark) 100%); }

  .mark-circle { position: absolute; border: 4px solid var(--ink); border-radius: 50%; }
  .brand-name { position: absolute; font-family: "Cormorant SC", serif; font-weight: 700; color: var(--ink); white-space: nowrap; letter-spacing: 1px; }
  .tagline { position: absolute; font-family: "Cormorant SC", serif; font-weight: 700; color: var(--ink); font-size: 13px; letter-spacing: .5px; display: flex; align-items: center; gap: 8px; white-space: nowrap; }
  .tagline::before, .tagline::after { content: ""; display: block; width: 50px; height: 2px; background: var(--ink); }
  .rule { position: absolute; height: 3px; background: var(--ink); }
  .site-url { position: absolute; font-family: "Cormorant SC", serif; font-weight: 500; color: var(--ink-soft); white-space: nowrap; }

  .front .mark-circle { left: 219px; top: 62px; width: 154px; height: 154px; }
  .front .brand-name { left: 0; width: 598px; text-align: center; top: 222px; font-size: 46px; }
  .front .tagline { left: 0; width: 598px; justify-content: center; top: 276px; }
  .front .rule { left: 110px; width: 376px; top: 309px; }
  .front .site-url { left: 0; width: 598px; text-align: center; top: 326px; font-size: 24px; }

  .back .mark-circle { left: 59px; top: 67px; width: 88px; height: 88px; }
  .back .brand-name { left: 158px; top: 82px; font-size: 42px; }
  .back .tagline { left: 158px; width: 380px; justify-content: center; top: 136px; }

  .story { position: absolute; left: 30px; width: 538px; top: 178px; text-align: center;
    font-family: "Shadows Into Light", cursive; font-size: 17px; line-height: 21px; color: var(--ink-soft); white-space: nowrap; }
  .story p + p { margin-top: 14px; }

  .contact-phone { position: absolute; left: 0; width: 598px; text-align: center; top: 632px;
    font-family: "Cormorant SC", serif; font-weight: 500; font-size: 25px; color: var(--ink); font-variant-numeric: lining-nums; }
  .contact-note { position: absolute; left: 0; width: 598px; text-align: center; top: 662px;
    font-family: "Cormorant SC", serif; font-weight: 500; font-size: 14px; color: var(--ink-soft); }
  .back .site-url { left: 0; width: 598px; text-align: center; top: 706px; font-size: 22px; }
  .back .rule--left { left: 0; width: 143px; top: 719px; }
  .back .rule--right { left: 453px; width: 145px; top: 719px; }
</style>
</head>
<body>
<main class="canvas">
  <section class="side side--front front">
    <div class="front-photo" role="img" aria-label="Photo of a young white husky-type dog standing on coastal rocks beside a yellow kayak, sea and blue sky behind"></div>
    <div class="mark-circle"></div>
    <div class="brand-name">Pawsome Keepers</div>
    <div class="tagline">Training * Dog Walking * Pet Sitting</div>
    <div class="rule"></div>
    <div class="site-url">PawsomeKeepers-example.com</div>
  </section>

  <section class="side side--back back">
    <div class="mark-circle"></div>
    <div class="brand-name">Pawsome Keepers</div>
    <div class="tagline">Training * Dog Walking * Pet Sitting</div>

    <div class="story">
      <p>I have been in love with dogs since I was a kid.<br>My favorite movie is still Harbor Hounds.</p>
      <p>Dogs can be our friends, our support system, our<br>motivation, and our family. I believe with today's busy<br>lifestyle most people want the best for their animals,<br>but simply don't have the time or energy to provide<br>everything they might have imagined for their companions.<br>That's where Pawsome Keepers comes in.</p>
      <p>I started working professionally with animals in 2010,<br>and quickly realized this was the passion I had been<br>searching for. I feel lucky to bring animals closer with<br>their people and vice versa.</p>
      <p>I offer training walks, one-on-one training sessions, and<br>overnight pet sitting in your home, with picture updates<br>daily by text or email. I am Blue Lantern and Critter Rescue<br>AID and CPR certified, and insured through Furbrook Guardians.<br>We are a green business: your file is kept online with all<br>vet info and house notes. Please contact me to<br>set up a free meet-and-greet today.</p>
    </div>

    <div class="contact-phone">(555) 123-4567</div>
    <div class="contact-note">CALL NOW FOR MORE INFORMATION</div>
    <div class="rule rule--left"></div>
    <div class="site-url">PawsomeKeepers-example.com</div>
    <div class="rule rule--right"></div>
  </section>
</main>
</body>
</html>
```